High-end law practice specializing in closely held business succession planning and complex estates

Solo practitioner whose practice specializes in high-net worth, complex estate planning needs muliple versions of letterhead black and white, please. Letterhead should incorporate slogan, "Protecting your family business is my business," for one and "Complex Estate Planning"; third with no slogan. All for The Law Office of Marguerite Elaine Haskett, PC, 418 Cedar Hollow Ln., Newport News, Virginia 23847, Tel. 757-481-5390 Fax tbd email: marguerite@mehcounsel.example; Marguerite Elaine Haskett, Esq., principal, licensed in VA, NY, DC
Updates

Project Deadline Extended
Reason: My internet service went down and I can only view designs on my smart phone -- it's just too hard to review. So sorry! Working with my ISP now. Please be patient!

Target Market(s)

High net worth clients with complex estate planning needs, family businesses, family farmers, family foresters -- people with unique estate/succession planning needs who need a specialist who understands them.

Industry/Entity Type

Business

Font styles to use
Script

Requirements
Must have
• A high-end look and feel, connoting trustworthiness, special knowledge, and expertise.

```html
<!DOCTYPE html>
<html lang="en">
<head>
<meta charset="utf-8">
<title>The Law Office of Marguerite Elaine Haskett, PC — Letterhead</title>
<link rel="stylesheet" href="https://fonts.googleapis.com/css2?family=Roboto+Slab:wght@300;400&display=swap">
<style>
  :root {
    --ink: #373435;
    --paper: #ffffff;
    --rule: #4a4748;
    --placeholder: #e4e3e3;
  }
  html, body {
    margin: 0;
    padding: 0;
    overflow: hidden;
    background: var(--paper);
  }
  .letterhead {
    position: relative;
    width: 849px;
    height: 1200px;
    box-sizing: border-box;
    border: 1px solid var(--rule);
    background: var(--paper);
    overflow: hidden;
    font-family: "Roboto Slab", Georgia, serif;
    font-weight: 300;
    color: var(--ink);
  }
  .brand-mark {
    position: absolute;
    left: 42px;
    top: 70px;
    width: 80px;
    height: 80px;
    box-sizing: border-box;
    border: 2px solid var(--ink);
    border-radius: 50%;
  }
  .firm-name {
    position: absolute;
    left: 134px;
    top: 76px;
    margin: 0;
    line-height: 1;
  }
  .firm-name .prefix {
    display: block;
    font-size: 21px;
    font-weight: 300;
  }
  .firm-name .principal {
    display: block;
    margin-top: 5px;
    font-size: 21px;
    font-weight: 400;
    letter-spacing: 0.3px;
  }
  .firm-credentials {
    position: absolute;
    left: 134px;
    top: 126px;
    margin: 0;
    font-size: 15px;
    letter-spacing: 0.2px;
  }
  .practice-icons {
    position: absolute;
    left: 460px;
    top: 66px;
    width: 370px;
    height: 42px;
    background: var(--placeholder);
  }
  .slogan-bar {
    position: absolute;
    left: 433px;
    top: 121px;
    width: 414px;
    height: 24px;
    background: var(--ink);
    color: var(--paper);
    font-size: 16px;
    line-height: 24px;
    text-align: center;
  }
  .footer-wave {
    position: absolute;
    left: 0;
    bottom: 0;
    display: block;
  }
  .footer-contact {
    position: absolute;
    left: 0;
    width: 100%;
    margin: 0;
    text-align: center;
    color: var(--paper);
    font-size: 14px;
    font-weight: 300;
  }
  .footer-contact.address { top: 1130px; }
  .footer-contact.lines { top: 1157px; }
  .footer-contact .sep { padding: 0 4px; }
</style>
</head>
<body>
  <div class="letterhead">
    <div class="brand-mark" aria-hidden="true"></div>

    <h1 class="firm-name">
      <span class="prefix">The Law Office of</span>
      <span class="principal">Marguerite Elaine Haskett, PC</span>
    </h1>
    <p class="firm-credentials">Esq., principal, licensed in VA, NY, DC</p>

    <div class="practice-icons" role="img" aria-label="Row of practice-area icons: oath on a book, hands, gavel, scales of justice, calculator, family, passport, handshake"></div>
    <div class="slogan-bar">Protecting your family business is my business.</div>

    <svg class="footer-wave" width="849" height="150" viewBox="0 1050 849 150" aria-hidden="true">
      <path d="M0 1112 Q 480 1118 849 1054 L849 1200 L0 1200 Z" fill="var(--ink)"/>
    </svg>
    <p class="footer-contact address">Address: 418 Cedar Hollow Ln., Newport News, Virginia 23847,</p>
    <p class="footer-contact lines">Telephone: 757-481-5390<span class="sep">|</span>Fax: 757-555-014-2290<span class="sep">|</span>E-mail: marguerite@mehcounsel.example<span class="sep">|</span>Website: www.mehcounsel.example</p>
  </div>
</body>
</html>
```